Software Consulting Business Needs a Powerpoint Design

We need a powerpoint template design for a software consulting company called Tessel7, that we can use for a corporate overview presentation.

Our website/logo can be found at www.tessel7-demo.net which should give you a good idea of our color scheme.

Here is a link to a zip file with the logos in AI format:

http://www.tessel7-demo.net/logo/T7_Logo_Illustrator.zip

Here is a link to the Din font:

http://www.tessel7-demo.net/logo/Din.zip

Sorry for delay. I was on vacation. A decision will be made by end of the week. Thanks!

Software

```html
<!DOCTYPE html>
<html lang="en">
<head>
<meta charset="utf-8">
<title>Tessel7 – Company Presentation Template</title>
<link href="https://fonts.googleapis.com/css2?family=Barlow:wght@400;500;600;700&display=swap" rel="stylesheet">
<style>
:root{
  --page:#e6e6e6;
  --navy:#252e3c;
  --navy-deep:#1f2733;
  --band:#2c3748;
  --red:#e3221f;
  --ink:#333a44;
  --white:#ffffff;
}
*{box-sizing:border-box;margin:0;padding:0}
html,body{width:1200px;height:920px;overflow:hidden;background:var(--page)}
body{font-family:"Barlow",Arial,sans-serif;color:var(--ink);position:relative}
.slide{position:absolute;width:285px;height:214px;background:var(--white);box-shadow:0 1px 4px rgba(0,0,0,.35);overflow:hidden}
.slide.dark{background:radial-gradient(ellipse at 50% 40%,#2a3444 0%,var(--navy) 60%,var(--navy-deep) 100%)}
.c1{left:13px}.c2{left:309px}.c3{left:605px}.c4{left:901px}
.r1{top:9px}.r2{top:238px}.r3{top:467px}.r4{top:696px}

.header{position:absolute;left:0;top:0;width:100%;height:30px;background:linear-gradient(180deg,#303b4d,var(--band))}
.header h2{position:absolute;left:18px;top:16px;font-size:10px;font-weight:400;color:var(--white)}

.footer-lines{position:absolute;left:0;width:100%;bottom:8px;height:4px;border-top:1px solid var(--red);border-bottom:1px solid var(--red)}
.footer-text{position:absolute;bottom:1px;left:10px;right:10px;font-size:3.6px;color:var(--red);display:flex;justify-content:space-between}
.footer-text span:nth-child(2){margin-right:90px}
.corner-mark{position:absolute;left:0;bottom:14px;width:21px;height:16px;background:var(--navy);display:flex;align-items:center;justify-content:center;gap:1px}
.corner-mark i{width:3px;height:3px;background:var(--red);display:block}
.corner-mark b{font-size:2.8px;color:var(--white);font-weight:600;letter-spacing:.2px}
.dark .footer-lines{border-bottom:none;bottom:11px;height:0}

.body{position:absolute;left:18px;right:16px;top:40px;font-size:4.6px;line-height:1.3}
.body h3{color:var(--red);font-size:5px;font-weight:600;margin:4px 0 1px}
.body ul{list-style:none}
.body li{padding-left:6px;position:relative}
.body li::before{content:"•";position:absolute;left:0;color:var(--red)}
.body li.sub{padding-left:12px}
.body li.sub::before{left:6px}
.rule{border-top:1px solid #cfd2d6;margin:6px 0 4px}
.cols{display:flex;gap:24px}
.reason{display:flex;gap:5px;margin:3px 0 5px}
.reason b{flex:0 0 8px;height:8px;background:var(--navy);color:var(--white);font-size:5px;display:flex;align-items:center;justify-content:center}

.brand{font-weight:600;color:var(--white);letter-spacing:1.5px}
.title-block{position:absolute;left:0;width:100%;text-align:center;color:var(--white)}
.brand-row{display:flex;align-items:center;justify-content:center;gap:6px}
.brand-row i{width:9px;height:9px;background:var(--red);display:block}

.agenda h2{position:absolute;left:20px;top:47px;font-size:10px;font-weight:400;color:var(--white)}
.agenda ul{position:absolute;left:18px;top:71px;width:252px;list-style:none;font-size:5.6px;color:var(--white)}
.agenda li{height:11.5px;line-height:11px;padding-left:9px;position:relative}
.agenda li::before{content:"";position:absolute;left:3px;top:4px;width:3px;height:3px;background:var(--red);transform:rotate(45deg)}
.agenda li.current{outline:1px solid var(--red)}

.products{position:absolute;left:18px;top:47px;display:grid;grid-template-columns:repeat(3,79px);gap:7px 9px}
.product{border:1px solid #f09a98;height:58px;padding:2px 3px;font-size:3.4px;line-height:1.25;box-shadow:0 1px 1px rgba(0,0,0,.1)}
.product h4{color:var(--red);font-size:4.4px;font-weight:600;margin-bottom:1px}

.offices{position:absolute;left:32px;top:63px}
.office{display:flex;align-items:center;gap:20px;height:30px;margin-bottom:11px}
.office .city{width:60px;height:30px;background:var(--red);border-radius:2px;color:var(--white);font-size:5.2px;display:flex;align-items:center;justify-content:center;box-shadow:0 1px 2px rgba(0,0,0,.3)}
.office ul{list-style:none;font-size:4.8px;line-height:1.6}
.office li::before{content:"• ";color:var(--red)}

.bullets-row{position:absolute;left:48px;display:flex;align-items:center;gap:30px}
.bullets-row .dot{width:31px;height:31px;border-radius:50%;background:var(--red);color:var(--white);font-size:4.2px;font-weight:600;display:flex;align-items:center;justify-content:center;box-shadow:0 1px 2px rgba(0,0,0,.3)}
.bullets-row ul{list-style:none;font-size:4.6px;line-height:1.95}
.bullets-row li::before{content:"• ";color:var(--red)}

.pics{position:absolute;left:16px;top:63px;display:flex;gap:10px}
.pic{width:80px;text-align:center;font-size:5.4px}
.pic .disc{width:80px;height:80px;border-radius:50%;margin-bottom:10px;box-shadow:0 1px 3px rgba(0,0,0,.3)}
.disc.pattern{background:radial-gradient(circle,#f7b9b5,#e9605a)}
.disc.mark{background:var(--navy);display:flex;align-items:center;justify-content:center;color:var(--white);font-size:8px;font-weight:600;letter-spacing:1px}
.disc.plain{background:radial-gradient(circle,#ffffff 35%,#f3d0ce)}
</style>
</head>
<body>

<section class="slide dark c1 r1">
  <div class="title-block" style="top:79px">
    <div class="brand-row"><i></i><span class="brand" style="font-size:15px">TESSEL7</span></div>
  </div>
  <div class="title-block" style="top:125px;font-size:11px">Company Presentation</div>
  <div class="title-block" style="top:167px;font-size:6px">6 Feb 2013</div>
  <div class="footer-lines"></div>
  <div class="title-block" style="bottom:2px;font-size:4px;color:var(--red)">tessel7.com</div>
</section>

<section class="slide c2 r1">
  <header class="header"><h2>Tessel7 – The Company</h2></header>
  <div class="body">
    <h3>About us</h3>
    <ul>
      <li>We are a software company specializing in enterprise technology.</li>
      <li>Founded in 2007, we deliver our products, world-class services, customized solutions, and timely support across all sectors of industry.</li>
    </ul>
    <h3>Why Us</h3>
    <div class="reason"><b>F</b><p>Tessel7 delivers broad industry experience to your project. Our combined talent and years of experience in enterprise software deployment can help you get better value from your technology investment.</p></div>
    <div class="reason"><b>A</b><p>A smaller team and focused attention means you see efficient and effective results. We use the latest technology to streamline our own operations for cost effective performance.</p></div>
    <div class="reason"><b>C</b><p>Customer satisfaction is our main goal. In order to reach this goal we provide clear communication and a fast turnaround time that does not compromise the quality of our work.</p></div>
    <div class="reason"><b>T</b><p>Technology issues can affect many different aspects of your business. Our team members are not only technology professionals but also business professionals, so we are able to give you a full picture outlook and strategy for your organization.</p></div>
  </div>
  <div class="corner-mark"><i></i><b>TESSEL7</b></div>
  <div class="footer-lines"></div>
  <div class="footer-text"><span>Copyright © 2013 Tessel7</span><span>tessel7.com</span><span>2</span></div>
</section>

<section class="slide dark agenda c3 r1">
  <h2>Agenda</h2>
  <ul><li class="current">Our Services</li><li>Our Products</li><li>Contact Us</li></ul>
  <div class="corner-mark" style="background:none"><i></i><b>TESSEL7</b></div>
  <div class="footer-lines"></div>
  <div class="footer-text"><span>Copyright © 2013 Tessel7</span><span>tessel7.com</span><span>3</span></div>
</section>

<section class="slide c4 r1">
  <header class="header"><h2>Services – Enterprise 2.0</h2></header>
  <div class="body" style="top:49px">
    <h3>Why Tessel7?</h3>
    <ul>
      <li>Tessel7 offers best-in-class consulting services for the Enterprise 2.0 space.</li>
      <li>We emphasize quality in all consulting engagements and treat each customer with the utmost care.</li>
      <li>Our services team is comprised of consultants with years of deployment experience in a variety of client industries, geographies, and organizational sizes.</li>
      <li>Not only will you receive flawless delivery from our professional service staff, but qualified advisors to aid in risk management for your project.</li>
    </ul>
    <div class="rule"></div>
    <h3>Service Offerings:</h3>
    <div class="cols">
      <ul><li>Initial implementation and installation</li><li>Product Upgrades</li><li>Portal/Content Migrations</li><li>Infrastructure and Architecture review</li></ul>
      <ul><li>Environment health checks</li><li>Custom Portal development</li><li>Portal governance</li><li>Training</li></ul>
    </div>
  </div>
  <div class="corner-mark"><i></i><b>TESSEL7</b></div>
  <div class="footer-lines"></div>
  <div class="footer-text"><span>Copyright © 2013 Tessel7</span><span>tessel7.com</span><span>4</span></div>
</section>

<section class="slide c1 r2">
  <header class="header"><h2>Services – Operational Intelligence</h2></header>
  <div class="body" style="top:48px">
    <h3>Why Tessel7?</h3>
    <ul><li>Tessel7 provides services in the Operational Intelligence space to help your organization structure your data in an effective way to allow you to make informed decisions with live data.</li></ul>
    <div class="rule" style="margin:8px 0"></div>
    <h3>Service Offerings:</h3>
    <ul>
      <li>Our deployment strategy includes:</li>
      <li class="sub">Identifying Valuable Fields from Your Data</li>
      <li class="sub">Structuring Your Data</li>
      <li class="sub">Creating an Enterprise Taxonomy</li>
      <li class="sub">Setting up Roles and Provisioning</li>
      <li class="sub">Limiting access through User Interfaces</li>
      <li class="sub">Creating Dashboards for Quick Access to Information</li>
    </ul>
  </div>
  <div class="corner-mark"><i></i><b>TESSEL7</b></div>
  <div class="footer-lines"></div>
  <div class="footer-text"><span>Copyright © 2013 Tessel7</span><span>tessel7.com</span><span>5</span></div>
</section>

<section class="slide c2 r2">
  <header class="header"><h2>Services – Operational Intelligence</h2></header>
  <div class="body" style="top:48px">
    <h3>Why Tessel7?</h3>
    <ul>
      <li>Tessel7 is a Corvane certified partner whose WEM consulting team is focused on providing solutions for customers planning to deploy a site based on these platforms.</li>
      <li>Our experts include solution architects, technical architects, lead developers, and other supporting members.</li>
      <li>In addition to solution design, development, and staff augmentation, we have conducted architecture, developer, and system administration training classes.</li>
      <li>We have led major initiatives to modernize best practices, including the current standard for FlowPortal Sites architecture, the Keystone Site Foundation (KSF).</li>
    </ul>
    <h3>Service Offerings:</h3>
    <div class="cols">
      <ul><li>Web Strategy Development</li><li>Initial Implementation and Installation</li><li>Product Upgrades</li><li>Migrations from Different Systems</li><li>Infrastructure and Architecture review</li></ul>
      <ul><li>Environment Health Checks</li><li>Content Personalization</li><li>Taxonomy Development</li><li>Training</li><li>Workshops</li></ul>
    </div>
  </div>
  <div class="corner-mark"><i></i><b>TESSEL7</b></div>
  <div class="footer-lines"></div>
  <div class="footer-text"><span>Copyright © 2013 Tessel7</span><span>tessel7.com</span><span>6</span></div>
</section>

<section class="slide dark agenda c3 r2">
  <h2>Agenda</h2>
  <ul><li>Our Services</li><li class="current">Our Products</li><li>Contact Us</li></ul>
  <div class="corner-mark" style="background:none"><i></i><b>TESSEL7</b></div>
  <div class="footer-lines"></div>
  <div class="footer-text"><span>Copyright © 2013 Tessel7</span><span>tessel7.com</span><span>7</span></div>
</section>

<section class="slide c4 r2">
  <header class="header"><h2>Our Products</h2></header>
  <div class="products">
    <div class="product"><h4>FormCrafter</h4><p>Stemming from the need to allow users to create uniform and structured web forms quickly and easily, we created FormCrafter to easily create, poll, collect, and organize online forms.</p></div>
    <div class="product"><h4>DocNavigator</h4><p>Manage your FlowPortal collaboration documents with grace and ease. Control your documents quickly and easily. Navigate and administer folders more effectively using the latest web technologies.</p></div>
    <div class="product"><h4>Sentinel</h4><p>Sentinel will monitor criteria specific to FlowPortal components and alert you when something is amiss. Sentinel can notify system administrators whenever a back-end service has crashed or recovered.</p></div>
    <div class="product"><h4>Liaison</h4><p>Liaison exists to bring your contacts, appointments, and email into the portal. Whether it is a Mailhub server or a mail service, have your mail account at your disposal.</p></div>
    <div class="product"><h4>FeedDesk</h4><p>Populate portlets with your favorite RSS news feeds or let everyone drop in their own daily reads. FeedDesk captures and archives feeds and keeps track of new articles.</p></div>
    <div class="product"><h4>Custom Products</h4><p>Have a product idea not listed here? Let us know and learn about our co-funded development model!</p></div>
  </div>
  <div class="corner-mark"><i></i><b>TESSEL7</b></div>
  <div class="footer-lines"></div>
  <div class="footer-text"><span>Copyright © 2013 Tessel7</span><span>tessel7.com</span><span>8</span></div>
</section>

<section class="slide dark agenda c1 r3">
  <h2>Agenda</h2>
  <ul><li>Our Services</li><li>Our Products</li><li class="current">Contact Us</li></ul>
  <div class="corner-mark" style="background:none"><i></i><b>TESSEL7</b></div>
  <div class="footer-lines"></div>
  <div class="footer-text"><span>Copyright © 2013 Tessel7</span><span>tessel7.com</span><span>9</span></div>
</section>

<section class="slide c2 r3">
  <header class="header"><h2>Contact Us</h2></header>
  <div class="offices">
    <div class="office"><div class="city">New York, NY</div><ul><li>Contact Person</li><li>E-mail</li><li>Phone number</li></ul></div>
    <div class="office"><div class="city">Washington, DC</div><ul><li>Contact Person</li><li>E-mail</li><li>Phone number</li></ul></div>
    <div class="office"><div class="city">Toronto, ON</div><ul><li>Contact Person</li><li>E-mail</li><li>Phone number</li></ul></div>
  </div>
  <div class="corner-mark"><i></i><b>TESSEL7</b></div>
  <div class="footer-lines"></div>
  <div class="footer-text"><span>Copyright © 2013 Tessel7</span><span>tessel7.com</span><span>10</span></div>
</section>

<section class="slide dark c3 r3">
  <div class="title-block" style="top:78px">
    <div class="brand-row"><i></i><span class="brand" style="font-size:15px">TESSEL7</span></div>
  </div>
  <div class="title-block" style="top:124px;font-size:11px">Thank you for your attention!</div>
  <div class="footer-lines"></div>
  <div class="title-block" style="bottom:2px;font-size:4px;color:var(--red)">tessel7.com</div>
</section>

<section class="slide dark c1 r4">
  <div class="title-block" style="top:102px;font-size:9.5px;color:var(--red)">Other Slide Design Templates Included</div>
  <div class="corner-mark" style="background:none"><i></i><b>TESSEL7</b></div>
  <div class="footer-lines"></div>
  <div class="footer-text"><span>Copyright © 2013 Tessel7</span><span>tessel7.com</span><span>12</span></div>
</section>

<section class="slide c2 r4">
  <header class="header"><h2>Graph slide</h2></header>
  <svg style="position:absolute;left:0;top:52px" width="285" height="130" viewBox="0 0 285 130" font-family="Barlow, Arial, sans-serif">
    <text x="23" y="5" font-size="5" font-weight="600" fill="#333a44">Graph Title</text>
    <line x1="22" y1="8" x2="134" y2="8" stroke="#c9ccd0" stroke-width=".6"/>
    <text x="163" y="5" font-size="5" font-weight="600" fill="#333a44">Comments</text>
    <line x1="162" y1="8" x2="265" y2="8" stroke="#c9ccd0" stroke-width=".6"/>
    <g font-size="4" fill="#333a44" text-anchor="end">
      <text x="20" y="21">5</text><text x="20" y="37">4</text><text x="20" y="53">3</text>
      <text x="20" y="69">2</text><text x="20" y="85">1</text><text x="20" y="101">0</text>
    </g>
    <line x1="24" y1="18" x2="24" y2="100" stroke="#333" stroke-width=".5"/>
    <line x1="24" y1="100" x2="135" y2="100" stroke="#333" stroke-width=".5"/>
    <g font-size="4" fill="#333a44" text-anchor="middle">
      <text x="35" y="107">1</text><text x="57" y="107">2</text><text x="79" y="107">3</text><text x="101" y="107">4</text><text x="123" y="107">5</text>
    </g>
    <polyline points="35,36 57,60 79,36 101,60 123,28" fill="none" stroke="#222" stroke-width="1"/>
    <g fill="#222"><circle cx="35" cy="36" r="1.3"/><circle cx="57" cy="60" r="1.3"/><circle cx="79" cy="36" r="1.3"/><circle cx="101" cy="60" r="1.3"/><circle cx="123" cy="28" r="1.3"/></g>
    <polyline points="35,60 57,28 79,68 101,66 123,44" fill="none" stroke="#e3221f" stroke-width="1"/>
    <g fill="#e3221f"><circle cx="35" cy="60" r="1.3"/><circle cx="57" cy="28" r="1.3"/><circle cx="79" cy="68" r="1.3"/><circle cx="101" cy="66" r="1.3"/><circle cx="123" cy="44" r="1.3"/></g>
    <line x1="50" y1="118" x2="60" y2="118" stroke="#222"/><circle cx="55" cy="118" r="1.2" fill="#222"/>
    <text x="62" y="119.5" font-size="4" fill="#333a44">Series 1</text>
    <line x1="83" y1="118" x2="93" y2="118" stroke="#e3221f"/><circle cx="88" cy="118" r="1.2" fill="#e3221f"/>
    <text x="95" y="119.5" font-size="4" fill="#333a44">Series 2</text>
    <g font-size="4.6" fill="#333a44">
      <text x="166" y="20">Lorem ipsum dolor sit amet, consectetur</text><text x="166" y="25.5">adipiscing elit.</text>
      <text x="166" y="38">Lorem ipsum dolor sit amet, consectetur</text><text x="166" y="43.5">adipiscing elit.</text>
      <text x="166" y="56">Lorem ipsum dolor sit amet, consectetur</text><text x="166" y="61.5">adipiscing elit.</text>
      <text x="166" y="74">Lorem ipsum dolor sit amet, consectetur</text><text x="166" y="79.5">adipiscing elit.</text>
    </g>
    <g fill="#e3221f"><circle cx="163" cy="18.5" r=".9"/><circle cx="163" cy="36.5" r=".9"/><circle cx="163" cy="54.5" r=".9"/><circle cx="163" cy="72.5" r=".9"/></g>
  </svg>
  <div class="corner-mark"><i></i><b>TESSEL7</b></div>
  <div class="footer-lines"></div>
  <div class="footer-text"><span>Copyright © 2013 Tessel7</span><span>tessel7.com</span><span>13</span></div>
</section>

<section class="slide c3 r4">
  <header class="header"><h2>Bullet slide</h2></header>
  <div class="bullets-row" style="top:64px"><div class="dot">Bullet 1</div><ul><li>Lorem ipsum dolor sit amet, consectetur adipiscing elit.</li><li>Lorem ipsum dolor sit amet, consectetur adipiscing elit.</li><li>Lorem ipsum dolor sit amet, consectetur adipiscing elit.</li></ul></div>
  <div class="bullets-row" style="top:105px"><div class="dot">Bullet 2</div><ul><li>Lorem ipsum dolor sit amet, consectetur adipiscing elit.</li><li>Lorem ipsum dolor sit amet, consectetur adipiscing elit.</li><li>Lorem ipsum dolor sit amet, consectetur adipiscing elit.</li></ul></div>
  <div class="bullets-row" style="top:146px"><div class="dot">Bullet 3</div><ul><li>Lorem ipsum dolor sit amet, consectetur adipiscing elit.</li><li>Lorem ipsum dolor sit amet, consectetur adipiscing elit.</li><li>Lorem ipsum dolor sit amet, consectetur adipiscing elit.</li></ul></div>
  <div class="corner-mark"><i></i><b>TESSEL7</b></div>
  <div class="footer-lines"></div>
  <div class="footer-text"><span>Copyright © 2013 Tessel7</span><span>tessel7.com</span><span>14</span></div>
</section>

<section class="slide c4 r4">
  <header class="header"><h2>Images slide</h2></header>
  <div class="pics">
    <div class="pic"><div class="disc pattern" role="img" aria-label="Round image placeholder with a red tiled pattern"></div>Lorem ipsum</div>
    <div class="pic"><div class="disc mark">TESSEL7</div>Lorem ipsum</div>
    <div class="pic"><div class="disc plain" role="img" aria-label="Round image placeholder with a red line graphic on white"></div>Lorem ipsum</div>
  </div>
  <div class="corner-mark"><i></i><b>TESSEL7</b></div>
  <div class="footer-lines"></div>
  <div class="footer-text"><span>Copyright © 2013 Tessel7</span><span>tessel7.com</span><span>15</span></div>
</section>

</body>
</html>
```